Bref créative
Healthcare apparel brand
Business Card, Letter head, Envelope, Email stationary
I need double sided standard sized Business Card [3.5" x 2"]
Bank Gothic and complimenting fonts
Professional
Marcus Pellandrou
CEO / Founder
482 Folwell Lane Suite B217
Santa Barbara, CA 93184
marcusp@brightloomwovens.example
www.veltunic.example
the corporation is Bright Loom Wovens LLC. The brand is Vel Tunic. I want to prominently display the green cross. Large. Maybe watermark. slogan "Fabrics for Change"
"A highly technical base layer which permanently guards against degradation from micro-organisms." and either one of
"A better choice" or "Just what the doctor ordered"
Logo

```html
<!DOCTYPE html>
<html lang="en">
<head>
<meta charset="utf-8">
<title>Vel Tunic Stationery</title>
<link href="https://fonts.googleapis.com/css2?family=Michroma&family=Open+Sans:wght@400;600&display=swap" rel="stylesheet">
<style>
  :root{
    --green:#8cc63f;
    --green-soft:#eef5e3;
    --ink:#3b3b3b;
    --muted:#8a8a8a;
    --line:#c9c9c9;
    --cell:#e4e4e4;
    --paper:#ffffff;
    --backdrop:#f2f2f2;
  }
  *{box-sizing:border-box;margin:0;padding:0}
  html,body{width:1200px;height:552px;overflow:hidden;background:var(--backdrop)}
  body{position:relative;font-family:"Open Sans",Arial,sans-serif;color:var(--ink)}
  .sheet{position:absolute;background:var(--paper);box-shadow:0 1px 4px rgba(0,0,0,.18);overflow:hidden}
  .brand{font-family:"Michroma",Arial,sans-serif;color:var(--ink);letter-spacing:.5px;display:flex;align-items:center;gap:6px;white-space:nowrap}
  .brand .mark{background:var(--green);display:inline-block}
  .tagline{font-size:5px;letter-spacing:2px;color:var(--muted);text-align:center;margin-top:3px}
  .watermark{position:absolute;background:var(--green-soft)}
  .footer{position:absolute;left:0;right:0;bottom:14px;text-align:center;font-size:5px;line-height:8px;color:var(--muted)}
  .bar{position:absolute;left:0;right:0;bottom:0;height:7px;background:var(--green)}

  /* fax */
  .fax{left:14px;top:14px;width:370px;height:519px}
  .fax .head{position:absolute;top:18px;left:0;right:0;display:flex;flex-direction:column;align-items:center}
  .fax .head .brand{font-size:14px}
  .fax .head .mark{width:12px;height:12px}
  .fax .title{position:absolute;top:50px;right:18px;font-size:9px;color:var(--ink);letter-spacing:1px}
  .fax-table{position:absolute;top:62px;left:18px;width:334px;border-collapse:collapse;font-size:6px}
  .fax-table td{border:1px solid var(--line);height:15px;padding:0 5px}
  .fax-table .label{width:34px}
  .fax-table .field{background:var(--cell);width:133px}
  .options{position:absolute;top:142px;left:18px;right:18px;display:flex;justify-content:space-between;font-size:6px}
  .options span::before{content:"";display:inline-block;width:6px;height:6px;border:1px solid var(--ink);margin-right:4px;vertical-align:-1px}
  .fax .watermark{left:95px;top:225px;width:180px;height:180px}

  /* letterhead */
  .letter{left:403px;top:14px;width:365px;height:519px}
  .letter .head{position:absolute;top:18px;left:0;right:0;display:flex;flex-direction:column;align-items:center}
  .letter .head .brand{font-size:14px}
  .letter .head .mark{width:12px;height:12px}
  .letter .watermark{left:92px;top:170px;width:180px;height:180px}

  /* cards */
  .card-front{left:773px;top:29px;width:168px;height:72px}
  .card-front .brand{position:absolute;left:8px;top:26px;font-size:7px}
  .card-front .mark{width:7px;height:7px}
  .card-front .who{position:absolute;left:84px;top:8px;font-size:4.5px;line-height:6.5px;color:var(--muted)}
  .card-front .who strong{color:var(--green);font-weight:600;display:block;font-size:5px}
  .card-front .contact{position:absolute;left:84px;top:30px;font-size:4px;line-height:6px;color:var(--muted)}
  .card-front .bar{height:4px}
  .card-back{left:950px;top:26px;width:168px;height:72px;background:var(--green);border-radius:6px}
  .card-back .brand{position:absolute;left:0;right:0;top:24px;justify-content:center;color:var(--paper);font-size:8px}
  .card-back .mark{width:8px;height:8px;background:var(--paper)}
  .card-back .line{position:absolute;left:0;right:0;top:10px;text-align:center;font-size:4.5px;color:var(--paper)}
  .card-back .url{position:absolute;left:0;right:0;bottom:8px;text-align:center;font-size:4.5px;color:var(--paper)}

  /* envelope front */
  .env-front{left:773px;top:125px;width:408px;height:187px}
  .env-front .brand{position:absolute;left:22px;top:38px;font-size:14px}
  .env-front .mark{width:12px;height:12px}
  .env-front .return{position:absolute;left:22px;top:62px;font-size:4.5px;color:var(--muted)}
  .env-front .watermark{right:40px;top:30px;width:120px;height:120px}
  .env-front .web{position:absolute;left:22px;bottom:12px;font-size:4.5px;color:var(--muted)}
  .env-front .bar{height:6px}

  /* envelope back */
  .env-back{left:773px;top:336px;width:408px;height:197px}
  .env-back svg.flap{position:absolute;left:0;top:0}
  .env-back .brand{position:absolute;left:0;right:0;top:40px;justify-content:center;color:var(--paper);font-size:9px}
  .env-back .mark{width:9px;height:9px;background:var(--paper)}
</style>
</head>
<body>

<section class="sheet fax" aria-label="Fax cover sheet">
  <div class="head">
    <div class="brand"><span class="mark"></span>VEL TUNIC</div>
    <div class="tagline">FABRICS FOR CHANGE</div>
  </div>
  <div class="title">FAX</div>
  <table class="fax-table">
    <tr><td class="label">To:</td><td class="field"></td><td class="label">From:</td><td class="field"></td></tr>
    <tr><td class="label">Fax:</td><td class="field"></td><td class="label">Pages:</td><td class="field"></td></tr>
    <tr><td class="label">Phone:</td><td class="field"></td><td class="label">Date:</td><td class="field"></td></tr>
    <tr><td class="label">Re:</td><td class="field"></td><td class="label">CC:</td><td class="field"></td></tr>
  </table>
  <div class="options">
    <span>Urgent</span><span>For Review</span><span>Please Comment</span><span>Please Reply</span><span>Please Recycle</span>
  </div>
  <div class="watermark"></div>
  <div class="footer">Bright Loom Wovens LLC · 482 Folwell Lane Suite B217 · Santa Barbara, CA 93184<br>T (805) 555-0142 · F (805) 555-0143 · www.veltunic.example</div>
  <div class="bar"></div>
</section>

<section class="sheet letter" aria-label="Letterhead">
  <div class="head">
    <div class="brand"><span class="mark"></span>VEL TUNIC</div>
    <div class="tagline">FABRICS FOR CHANGE</div>
  </div>
  <div class="watermark"></div>
  <div class="footer">Bright Loom Wovens LLC · 482 Folwell Lane Suite B217 · Santa Barbara, CA 93184<br>T (805) 555-0142 · F (805) 555-0143 · www.veltunic.example</div>
  <div class="bar"></div>
</section>

<section class="sheet card-front" aria-label="Business card front">
  <div class="brand"><span class="mark"></span>VEL TUNIC</div>
  <div class="who"><strong>Marcus Pellandrou</strong>CEO / Founder</div>
  <div class="contact">482 Folwell Lane Suite B217<br>Santa Barbara, CA 93184<br>T (805) 555-0142<br>marcusp@brightloomwovens.example</div>
  <div class="bar"></div>
</section>

<section class="sheet card-back" aria-label="Business card back">
  <div class="line">A better choice</div>
  <div class="brand"><span class="mark"></span>VEL TUNIC</div>
  <div class="url">www.veltunic.example</div>
</section>

<section class="sheet env-front" aria-label="Envelope front">
  <div class="brand"><span class="mark"></span>VEL TUNIC</div>
  <div class="return">482 Folwell Lane Suite B217 · Santa Barbara, CA 93184</div>
  <div class="watermark"></div>
  <div class="web">www.veltunic.example</div>
  <div class="bar"></div>
</section>

<section class="sheet env-back" aria-label="Envelope back">
  <svg class="flap" width="408" height="197" viewBox="0 0 408 197">
    <path d="M0 0 H408 V18 L204 70 L0 18 Z" fill="var(--green)"/>
  </svg>
  <div class="brand" style="top:22px"><span class="mark"></span>VEL TUNIC</div>
</section>

</body>
</html>
```